New Zealand Export company needs business cards

We need new business cards to match our new logo for a company based in New Zealand who deal specifically with the Pacific Islands. We source, consolidate and ship products out of New Zealand to the Pacific Islands. Will attach our old ones and also new logo.
Would like the Islands we deal with and the areas of work we have access to, to be included on the business cards.

Contact Information for Business Card

T +64 9 571 3048
F +64 9 571 6285
12-18 Kowhai Lane, Drury, 2113
PO Box 814, Drury, Auckland 2247, New Zealand
www.falconfreight.example.nz
E sales@falconfreight.example.nz

Font styles to use
Sans Serif

Colors
85abd2
33a6d7
ffffff

Requirements
Must have
• A company of PWM

```html
<!DOCTYPE html>
<html lang="en">
<head>
<meta charset="utf-8">
<title>Falcon Freight – Business Card</title>
<link rel="stylesheet" href="https://fonts.googleapis.com/css2?family=Raleway:wght@400&family=Source+Sans+3:wght@400;700&display=swap">
<style>
  :root {
    --backdrop: #222629;
    --card: #f1f1f1;
    --brand-dark: #0b4a8c;
    --brand-light: #33a6d7;
    --band: #2563a0;
    --text-grey: #4a4a4a;
    --white: #ffffff;
  }
  * { margin: 0; padding: 0; box-sizing: border-box; }
  html, body { width: 1200px; height: 1176px; overflow: hidden; }
  body {
    background: var(--backdrop);
    position: relative;
    font-family: "Source Sans 3", sans-serif;
    color: var(--text-grey);
  }
  .card {
    position: absolute;
    left: 280px;
    width: 618px;
    height: 352px;
    background: var(--card);
    border-radius: 20px;
    overflow: hidden;
  }
  .card--front { top: 190px; }
  .card--back { top: 591px; }

  .brand {
    position: absolute;
    display: flex;
    align-items: center;
    gap: 10px;
    font-family: "Source Sans 3", sans-serif;
    font-weight: 700;
    color: var(--brand-dark);
    letter-spacing: 0.04em;
    white-space: nowrap;
  }
  .brand__mark { background: var(--brand-dark); flex: none; }
  .card--front .brand { left: 0; right: 0; top: 48px; justify-content: center; font-size: 28px; }
  .card--front .brand__mark { width: 26px; height: 26px; }

  .holder {
    position: absolute;
    right: 330px;
    top: 192px;
    text-align: right;
    font-family: "Raleway", sans-serif;
  }
  .holder__name { font-size: 24px; color: var(--text-grey); letter-spacing: 0.01em; }
  .holder__title { font-size: 15px; color: var(--brand-light); margin-top: 4px; }

  .divider {
    position: absolute;
    left: 309px;
    top: 167px;
    width: 2px;
    height: 101px;
    background: var(--band);
  }
  .contacts {
    position: absolute;
    left: 330px;
    top: 168px;
    list-style: none;
    font-size: 15px;
  }
  .contacts li { display: flex; align-items: center; height: 26px; }
  .contacts svg { width: 13px; height: 13px; margin-right: 9px; fill: var(--brand-light); flex: none; }

  .address-band {
    position: absolute;
    left: 0; right: 0; bottom: 0;
    height: 50px;
    background: var(--band);
    color: var(--white);
    font-size: 15px;
    line-height: 21px;
    text-align: center;
    padding-top: 4px;
  }

  .card--back .brand { left: 88px; top: 138px; font-size: 40px; gap: 16px; }
  .card--back .brand__mark { width: 40px; height: 40px; }
  .parent-note {
    position: absolute;
    left: 0; right: 0;
    top: 196px;
    text-align: center;
    font-size: 16px;
    color: var(--text-grey);
  }
</style>
</head>
<body>

  <section class="card card--front" aria-label="Business card front">
    <div class="brand"><span class="brand__mark"></span>FALCON FREIGHT</div>

    <div class="holder">
      <p class="holder__name">YOUR NAME</p>
      <p class="holder__title">JOB TITLE</p>
    </div>

    <div class="divider"></div>

    <ul class="contacts">
      <li><svg viewBox="0 0 16 16"><path d="M4 1l3 3-2 2c1 2 3 4 5 5l2-2 3 3-2 2C7 14 2 9 2 3z"/></svg>+64 9 571 3048</li>
      <li><svg viewBox="0 0 16 16"><path d="M4 1h7v4H4zM2 6h12v8H2zm3 2v1h2V8zm4 0v1h2V8zm-4 3v1h2v-1zm4 0v1h2v-1z"/></svg>+64 9 571 6285</li>
      <li><svg viewBox="0 0 16 16"><path d="M1 3h14v10H1zm1 1.2V5l6 4 6-4v-.8L8 8z"/></svg>sales@falconfreight.example.nz</li>
      <li><svg viewBox="0 0 16 16"><circle cx="8" cy="8" r="6.5" fill="none" stroke="#33a6d7" stroke-width="1.3"/><path d="M1.5 8h13M8 1.5c-3 3-3 10 0 13M8 1.5c3 3 3 10 0 13" fill="none" stroke="#33a6d7" stroke-width="1.1"/></svg>www.falconfreight.example.nz</li>
    </ul>

    <div class="address-band">
      <p>12-18 Kowhai Lane, Drury, 2113</p>
      <p>PO Box 814, Drury, Auckland 2247, New Zealand</p>
    </div>
  </section>

  <section class="card card--back" aria-label="Business card back">
    <div class="brand"><span class="brand__mark"></span>FALCON FREIGHT</div>
    <p class="parent-note">A company of PWM</p>
  </section>

</body>
</html>
```